New Business Card for General Contractor Marketing

Need a business card the is more like a marketing promotion of our services
Must be horizontal orientation, One Sided Only, Max font size, Organize the Services
#1 General Contractor for Realtors
Remodels – Renovations – Repairs
Water & Mold Damage Experts
Painting: Interior/ Exterior
Flooring: Wood / LVT / Carpet
Plumbing: Repairs & Upgrades
Electric: Lights & Energy Efficient Upgrades
Kitchen & Bath Remodels
Fast Inspections Repair Billed Thru Escrow
BrightHarborBuilds.com
555-418-2796

Industry/Entity Type

General Contractor

Contact Information for Business Card

One Sided Only: #1 General Contractor for Realtors Remodels – Renovations – Repairs Water & Mold Damage Experts Painting: Interior/ Exterior Flooring: Wood / LVT / Carpet Plumbing: Repairs & Upgrades Electric: Lights & Energy Efficient Upgrades Kitchen & Bath Remodels Fast Inspections Repair Billed Thru Escrow BrightHarborBuilds.com 555-418-2796

Colors
0054AA
0677BA
7BADD7
CADEEF
E8F1F8

Requirements
Must have
• One Sided Only: #1 General Contractor for Realtors Remodels – Renovations – Repairs Water & Mold Damage Experts Painting: Interior/ Exterior Flooring: Wood / LVT / Carpet Plumbing: Repairs & Upgrades Electric: Lights & Energy Efficient Upgrades Kitchen & Bath Remodels Fast Inspections Repair Billed Thru Escrow BrightHarborBuilds.com 555-418-2796

```html
<!DOCTYPE html>
<html lang="en">
<head>
<meta charset="utf-8">
<title>Bright Harbor Builds Inc. – Business Card</title>
<link href="https://fonts.googleapis.com/css2?family=Michroma&family=Montserrat:wght@300;400&family=Roboto:wght@400&display=swap" rel="stylesheet">
<style>
  :root {
    --navy: #0054AA;
    --blue: #0677BA;
    --sky: #7BADD7;
    --mist: #CADEEF;
    --ice: #E8F1F8;
    --white: #ffffff;
    --stage: #dfe3e8;
  }
  * { margin: 0; padding: 0; box-sizing: border-box; }
  html, body { width: 1200px; height: 780px; overflow: hidden; background: var(--stage); }
  .card {
    position: absolute; left: 75px; top: 90px; width: 1050px; height: 600px;
    background: var(--white); overflow: hidden;
    box-shadow: 0 10px 30px rgba(0,40,90,.25);
  }
  .card__bands { position: absolute; inset: 0; }
  .heading { font-family: "Michroma", sans-serif; text-transform: uppercase; }
  .detail { font-family: "Montserrat", sans-serif; font-weight: 300; text-transform: uppercase; letter-spacing: .04em; }

  .services { position: absolute; top: 44px; left: 44px; display: flex; gap: 34px; }
  .services__col { display: flex; flex-direction: column; gap: 16px; }
  .services__col + .services__col { border-left: 1.5px solid var(--blue); padding-left: 34px; }
  .service { display: flex; gap: 12px; align-items: flex-start; }
  .service__pin { width: 18px; height: 22px; margin-top: 4px; flex: none; }
  .service__name { color: var(--navy); font-size: 19px; line-height: 1.2; }
  .service__detail { color: var(--blue); font-size: 15px; margin-top: 3px; }

  .brand { position: absolute; top: 58px; right: 44px; width: 390px; text-align: right; }
  .brand__mark { display: inline-block; width: 22px; height: 22px; background: var(--navy); margin-bottom: 10px; }
  .brand__name { color: var(--navy); font-size: 27px; line-height: 1.25; }
  .website { position: absolute; top: 176px; right: 44px; color: var(--blue); font-size: 19px; letter-spacing: .06em; }

  .highlights { position: absolute; top: 236px; left: 60px; list-style: none; }
  .highlights li {
    font-family: "Roboto", sans-serif; color: var(--white); font-size: 24px; line-height: 1.38;
    padding-left: 26px; position: relative;
  }
  .highlights li::before {
    content: ""; position: absolute; left: 0; top: 12px; width: 11px; height: 11px;
    border-radius: 50%; background: var(--white);
  }

  .contact { position: absolute; top: 398px; left: 60px; }
  .contact__label { color: var(--sky); font-size: 20px; }
  .contact__phone { color: var(--navy); font-size: 38px; line-height: 1.2; }

  .tagline { position: absolute; left: 0; width: 100%; text-align: center; color: var(--white); }
  .tagline--services { top: 489px; font-size: 22px; }
  .tagline--realtors { top: 542px; font-size: 21px; color: var(--white); }
</style>
</head>
<body>
<main class="card">
  <svg class="card__bands" width="1050" height="600" viewBox="0 0 1050 600" aria-hidden="true">
    <rect x="0" y="0" width="1050" height="12" fill="var(--navy)"/>
    <rect x="0" y="12" width="1050" height="8" fill="var(--mist)"/>
    <rect x="540" y="160" width="510" height="58" fill="var(--mist)"/>
    <polygon points="0,218 560,218 640,300 560,382 0,382" fill="var(--blue)"/>
    <polygon points="560,218 640,300 560,382 590,382 670,300 590,218" fill="var(--sky)"/>
    <rect x="0" y="478" width="1050" height="52" fill="var(--blue)"/>
    <rect x="0" y="530" width="1050" height="56" fill="var(--sky)"/>
    <rect x="0" y="586" width="1050" height="14" fill="var(--navy)"/>
    <rect x="1020" y="20" width="14" height="458" fill="var(--navy)"/>
    <rect x="1034" y="20" width="16" height="458" fill="var(--mist)"/>
  </svg>

  <section class="services">
    <div class="services__col">
      <div class="service">
        <svg class="service__pin" viewBox="0 0 18 22" aria-hidden="true"><path d="M9 1a7 7 0 0 1 7 7c0 5-7 13-7 13S2 13 2 8a7 7 0 0 1 7-7z" fill="var(--sky)"/><circle cx="9" cy="8" r="2.6" fill="var(--white)"/></svg>
        <div><p class="service__name heading">Painting:</p><p class="service__detail detail">Interior / Exterior</p></div>
      </div>
      <div class="service">
        <svg class="service__pin" viewBox="0 0 18 22" aria-hidden="true"><path d="M9 1a7 7 0 0 1 7 7c0 5-7 13-7 13S2 13 2 8a7 7 0 0 1 7-7z" fill="var(--sky)"/><circle cx="9" cy="8" r="2.6" fill="var(--white)"/></svg>
        <div><p class="service__name heading">Flooring:</p><p class="service__detail detail">Wood / LVT / Carpet</p></div>
      </div>
    </div>
    <div class="services__col">
      <div class="service">
        <svg class="service__pin" viewBox="0 0 18 22" aria-hidden="true"><path d="M9 1a7 7 0 0 1 7 7c0 5-7 13-7 13S2 13 2 8a7 7 0 0 1 7-7z" fill="var(--sky)"/><circle cx="9" cy="8" r="2.6" fill="var(--white)"/></svg>
        <div><p class="service__name heading">Plumbing:</p><p class="service__detail detail">Repairs &amp; Upgrades</p></div>
      </div>
      <div class="service">
        <svg class="service__pin" viewBox="0 0 18 22" aria-hidden="true"><path d="M9 1a7 7 0 0 1 7 7c0 5-7 13-7 13S2 13 2 8a7 7 0 0 1 7-7z" fill="var(--sky)"/><circle cx="9" cy="8" r="2.6" fill="var(--white)"/></svg>
        <div><p class="service__name heading">Electric:</p><p class="service__detail detail">Lights &amp; Energy<br>Efficient Upgrades</p></div>
      </div>
    </div>
  </section>

  <header class="brand">
    <span class="brand__mark" aria-hidden="true"></span>
    <h1 class="brand__name heading">Bright Harbor<br>Builds Inc.</h1>
  </header>
  <p class="website detail">BrightHarborBuilds.com</p>

  <ul class="highlights">
    <li>Water &amp; Mold Damage Experts</li>
    <li>Kitchen &amp; Bath Remodels</li>
    <li>Fast Inspections Repair</li>
    <li>Billed Thru Escrow</li>
  </ul>

  <div class="contact">
    <p class="contact__label heading">Call/Text</p>
    <p class="contact__phone heading">555-418-2796</p>
  </div>

  <p class="tagline tagline--services heading">Remodels – Renovations – Repairs</p>
  <p class="tagline tagline--realtors heading">#1 General Contractor for Realtors</p>
</main>
</body>
</html>
```